Property investment company needs a letterhead design!

We are a new residential and commercial property investment company. Name of the company is Morvesta Group, LLC. We have a new logo and now we need letterhead! We prefer to have a professional and upscale appearance. We don't have any fixed requirements, so be creative! Thank you for considering this project. We are so excited to see what happens!

Target Market(s)

Professional

Industry/Entity Type

Real Estate Development

```html
<!DOCTYPE html>
<html lang="en">
<head>
<meta charset="utf-8">
<title>Morvesta Group Letterhead</title>
<link href="https://fonts.googleapis.com/css2?family=Poppins:wght@400;600;700&family=Questrial&display=swap" rel="stylesheet">
<style>
  :root {
    --navy: #0f2340;
    --sky: #1aa7e6;
    --ink: #2b2b2b;
    --paper-light: #f3f3f3;
    --paper-dark: #dedede;
    --rule: #555;
  }
  * { margin: 0; padding: 0; box-sizing: border-box; }
  html, body { width: 960px; height: 1200px; overflow: hidden; }
  body { background: var(--paper-dark); }
  .letterhead {
    position: relative;
    width: 960px; height: 1200px;
    background: linear-gradient(100deg, var(--paper-light) 0%, #e6e6e6 55%, var(--paper-dark) 100%);
    font-family: "Questrial", sans-serif;
    color: var(--ink);
  }
  .brand {
    position: absolute; left: 87px; top: 96px;
    display: flex; align-items: center; gap: 12px;
  }
  .brand-dot { width: 22px; height: 22px; border-radius: 50%; background: var(--sky); }
  .brand-name {
    font-family: "Poppins", sans-serif; font-weight: 700;
    font-size: 27px; letter-spacing: 0.5px; color: var(--navy); line-height: 1;
  }
  .contact {
    position: absolute; top: 111px; right: 78px;
    display: flex; font-family: "Poppins", sans-serif; font-size: 14.5px; line-height: 18px; color: var(--ink);
  }
  .contact-address { text-align: right; padding-right: 18px; border-right: 1px solid var(--rule); }
  .contact-web { font-weight: 600; letter-spacing: 0.6px; color: var(--navy); }
  .contact-lines { padding-left: 18px; }
  .contact-lines div { display: flex; align-items: center; gap: 6px; }
  .contact-lines svg { width: 11px; height: 11px; fill: var(--navy); }
  .greeting { position: absolute; left: 87px; top: 350px; font-size: 23px; }
  .body-copy {
    position: absolute; left: 87px; top: 417px; width: 791px;
    font-size: 13.8px; line-height: 20.3px; text-align: justify;
  }
  .body-copy p { margin-bottom: 20px; }
  .closing { position: absolute; left: 87px; top: 815px; font-size: 13.8px; }
  .signature {
    position: absolute; left: 87px; top: 845px; width: 125px; height: 70px;
    background: linear-gradient(90deg, #d2d2d2, #e2e2e2); border-radius: 4px;
  }
  .footer-band { position: absolute; left: 0; bottom: 0; width: 960px; height: 10px; }
</style>
</head>
<body>
<main class="letterhead">
  <header>
    <div class="brand">
      <span class="brand-dot"></span>
      <span class="brand-name">MORVESTA GROUP, LLC</span>
    </div>
    <div class="contact">
      <div class="contact-address">
        <div>2140 Alder Ridge Road</div>
        <div>Palmer, Alaska 99645</div>
        <div class="contact-web">www.morvesta.com</div>
      </div>
      <div class="contact-lines">
        <div><svg viewBox="0 0 24 24"><path d="M6.6 10.8a15 15 0 0 0 6.6 6.6l2.2-2.2a1 1 0 0 1 1-.25 11.4 11.4 0 0 0 3.6.6 1 1 0 0 1 1 1V20a1 1 0 0 1-1 1A17 17 0 0 1 3 4a1 1 0 0 1 1-1h3.5a1 1 0 0 1 1 1c0 1.25.2 2.45.6 3.6a1 1 0 0 1-.25 1z"/></svg>555-214-7730</div>
        <div><svg viewBox="0 0 24 24"><path d="M6 2h12v6H6zM3 9h18v9h-3v4H6v-4H3zM8 15v5h8v-5z"/></svg>555-214-7731</div>
        <div><svg viewBox="0 0 24 24"><path d="M2 5h20v14H2zm2 2v.5l8 5 8-5V7z"/></svg>info@morvesta.com</div>
      </div>
    </div>
  </header>

  <p class="greeting">Dear Mr. Hale,</p>

  <section class="body-copy">
    <p>Lorem ipsum dolor sit amet, consectetur adipiscing elit. Donec orci purus, luctus vitae dignissim eu, iaculis sed purus. Vivamus faucibus, ipsum nec aliquet viverra, leo mauris condimentum ligula, sit amet sagittis enim ligula quis arcu. Nam egestas tortor id nisi porttitor mattis. In tortor ante, ultricies in suscipit a, tempus non massa. Vivamus et auctor mi. Fusce vel massa nulla. Phasellus nec eros mauris, et scelerisque orci.</p>
    <p>Donec malesuada orci vitae nulla accumsan porta a id massa. Quisque accumsan iaculis magna sit amet fringilla. Maecenas consequat, magna eget tincidunt semper, odio nibh rutrum mi, id feugiat ante nisi eu risus. Vestibulum nunc orci, rhoncus a placerat in, ultricies in mi. Cras mattis varius eros, vel fringilla nisi suscipit eget. Quisque scelerisque sagittis nulla at porttitor.</p>
    <p>Sed id augue vitae urna euismod commodo aliquet a quam. Pellentesque arcu velit, cursus et malesuada ut, consequat et diam. Nullam erat sem, rhoncus id ullamcorper vitae, rhoncus et arcu. In ultricies ultricies nulla, ut rutrum nisi iaculis at. Donec eu magna a metus ornare faucibus. Fusce aliquet faucibus ultricies. Morbi semper, est id tincidunt gravida, sem arcu adipiscing lacus, ac bibendum nulla leo eu purus. Quisque nec diam sed risus consectetur a ccumsan quis quis nibh. Vestibulum id purus lorem.</p>
    <p>It is a long established fact that a reader will be distracted by the readable content of a page when looking at its layout. The point of using Lorem Ipsum is that it has a more-or-less normal distribution of letters, as opposed to using 'Content here, content here', making it look like readable English. Many desktop publishing packages</p>
  </section>

  <p class="closing">Sincerely,</p>
  <div class="signature" role="img" aria-label="Handwritten signature of the sender"></div>

  <svg class="footer-band" viewBox="0 0 960 10" preserveAspectRatio="none" aria-hidden="true">
    <polygon points="0,0 790,0 800,10 0,10" fill="var(--navy)"/>
    <polygon points="796,0 960,0 960,10 806,10" fill="#ffffff"/>
    <polygon points="802,0 960,0 960,10 812,10" fill="var(--sky)"/>
  </svg>
</main>
</body>
</html>
```